December online webinar for our coaching and mentoring business.

needing an email flyer and something to use on appropriate social media e.g. Instagram to promote our December half day webinar focusing on positive mindset, relationships and 2021 being a new year with new opportunities. For the feel of what we have done previously:
www.qlvgetaways.com.au
We will be using 2 guest speakers:
Dominic Farrow of 60Quests.com and
Marisa Holt, psychologist and both will need to be prominent on the marketing material we send out on email and use on social media.
The webinar will likely run Thursday December 10th from 12.30pm to 4.30pm AEST and will be hosted and facilitated by me and on behalf of Portwell Business Coaching.
I am thinking colour schemes and branding similar to what you see on the website above.
Pricing needs to be on the flyer - $750 + GST per person*
*enquire for multi booking discounts for 2 people or more

Target Market(s)

people looking for a boost before the year end and a fast start to 2021

Font styles to use
Sans Serif

Requirements
Must have
• see brief above
Nice to have
• see brief above
Should not have
• see brief above

```html
<!DOCTYPE html>
<html lang="en">
<head>
<meta charset="utf-8">
<title>December Webinar – Portwell Business Coaching</title>
<link href="https://fonts.googleapis.com/css2?family=Poppins:wght@400;500;600&display=swap" rel="stylesheet">
<style>
:root{
  --red:#ef3e33;
  --charcoal:#3e3e40;
  --panel:#f8f8f8;
  --topbar:#f4f4f4;
  --ink:#1d1d1d;
  --white:#ffffff;
  --photo-dark:#2f2f2f;
  --photo-warm:#e7c98a;
}
*{box-sizing:border-box;margin:0;padding:0}
html,body{width:1200px;height:2772px;overflow:hidden;background:var(--white);font-family:"Poppins",Arial,sans-serif;color:var(--ink)}
.canvas{position:relative;width:1200px;height:2772px}
.abs{position:absolute}

.browser-bar{left:0;top:0;width:1200px;height:75px;background:var(--topbar);font-family:Arial,Helvetica,sans-serif;font-size:21px;color:#333;text-align:center;line-height:66px}

.hero{left:112px;top:75px;width:976px;height:337px;background:var(--charcoal);overflow:hidden}
.hero svg{position:absolute;left:0;top:0}
.brand{left:45px;top:70px;color:var(--white);font-weight:600;font-size:30px;line-height:1.15;width:330px}
.hero-copy{right:22px;top:66px;text-align:right;color:var(--white)}
.hero-month{color:var(--red);font-weight:500;font-size:36px;line-height:1}
.hero-title{font-weight:600;font-size:86px;line-height:1;letter-spacing:1px;margin-top:4px}
.hero-theme{font-weight:600;font-size:47px;line-height:1.1;margin-top:20px}
.hero-sub{font-weight:500;font-size:31px;line-height:1.2;margin-top:2px}

.speakers{left:112px;top:412px;width:976px;height:840px;background:var(--panel)}
.section-title{position:absolute;left:0;width:976px;top:80px;text-align:center;font-size:36px;font-weight:500;letter-spacing:1px;color:#2b2b2b}
.section-rule{position:absolute;left:354px;top:139px;width:266px;height:6px;background:var(--red)}
.speaker{position:absolute;top:251px;width:450px;text-align:center}
.speaker.first{left:17px}
.speaker.second{left:467px}
.speaker .portrait{width:351px;height:351px;border-radius:50%;margin:0 auto}
.speaker-name{color:var(--red);font-size:39px;font-weight:400;margin-top:30px;line-height:1.2}
.speaker-role{font-size:26px;font-weight:500;line-height:1.3}
.speaker-site{font-size:22px;margin-top:6px}

.venue{left:112px;top:1252px;width:488px;height:342px;background:var(--charcoal);color:var(--white);padding:54px 0 0 62px}
.block-title{font-size:36px;font-weight:500;line-height:1}
.block-rule{width:131px;height:6px;background:var(--white);margin-top:18px}
.venue-line{font-size:26px;margin-top:16px;line-height:1.15}
.venue-line:first-of-type{margin-top:34px}
.venue-line b{font-weight:600}

.price{left:600px;top:1252px;width:488px;height:342px;background:var(--red);color:var(--white)}
.price-amount{position:absolute;left:48px;top:38px;font-size:118px;font-weight:600;line-height:1}
.price-gst{position:absolute;left:342px;top:118px;font-size:24px}
.price-unit{position:absolute;left:124px;top:150px;font-size:38px}
.price-note{position:absolute;left:36px;top:225px;width:420px;font-size:22px;line-height:1.6}

.host-photo{left:112px;top:1594px;width:488px;height:350px;background:linear-gradient(135deg,#e9e7e2,#c9c3bb 55%,var(--red) 100%)}
.host{left:600px;top:1594px;width:488px;height:350px;background:var(--charcoal);color:var(--white);padding:34px 0 0 18px}
.host .block-rule{width:131px}
.host-name{font-size:26px;font-weight:600;margin:40px 0 0 8px}
.host-company{font-size:22px;margin:16px 0 0 8px}

.cta{left:316px;top:1998px;width:566px;height:99px;background:var(--red);color:var(--white);font-size:36px;font-weight:500;text-align:center;line-height:99px;letter-spacing:.5px}

.footer{left:0;top:2191px;width:1200px;height:362px;background:var(--charcoal);text-align:center}
.footer-brand{position:absolute;left:0;width:1200px;top:70px;color:var(--red);font-size:52px;font-weight:600;line-height:1.1}
.footer-contact{position:absolute;left:0;width:1200px;top:250px;color:var(--red);font-size:22px;letter-spacing:1px}
.footer-contact span{margin:0 18px}

.social{top:2591px;width:75px;height:75px;border-radius:50%}
.social.one{left:414px;background:#4c6db4}
.social.two{left:513px;background:#74c8ef}
.social.three{left:613px;background:#c8183c}
.social.four{left:712px;background:#c41c2e}
</style>
</head>
<body>
<div class="canvas">
  <div class="abs browser-bar">Don’t see this email properly? View in web browser</div>

  <header class="abs hero">
    <svg width="976" height="337" viewBox="0 0 976 337" aria-hidden="true"><polygon points="0,0 615,0 0,337" fill="var(--red)"/></svg>
    <div class="abs brand">portwell business coaching</div>
    <div class="abs hero-copy">
      <div class="hero-month">DEC 2020</div>
      <div class="hero-title">WEBINAR</div>
      <div class="hero-theme">Positive Mindset, Relationships</div>
      <div class="hero-sub">&amp;2021 being a new year with new opportunities</div>
    </div>
  </header>

  <section class="abs speakers">
    <h2 class="section-title">OUR SPEAKERS</h2>
    <div class="section-rule"></div>
    <div class="speaker first">
      <div class="portrait" role="img" aria-label="Portrait of Dominic Farrow" style="background:radial-gradient(circle,#8a8a8a,var(--photo-dark))"></div>
      <div class="speaker-name">Dominic Farrow</div>
      <div class="speaker-role">Motivational Speaker</div>
      <div class="speaker-site">60Quests.com</div>
    </div>
    <div class="speaker second">
      <div class="portrait" role="img" aria-label="Portrait of Marisa Holt" style="background:radial-gradient(circle,#f1dcb0,var(--photo-warm) 60%,#2f6f95)"></div>
      <div class="speaker-name">Marisa Holt</div>
      <div class="speaker-role">Psychologist</div>
      <div class="speaker-site">marisaholtpsychology.com.au</div>
    </div>
  </section>

  <section class="abs venue">
    <div class="block-title">VENUE</div>
    <div class="block-rule"></div>
    <p class="venue-line"><b>Date:</b> 10th December, 2020</p>
    <p class="venue-line"><b>Time:</b> 12:30pm - 04:30 pm</p>
  </section>

  <section class="abs price">
    <div class="price-amount">$750</div>
    <div class="price-gst">+ GST</div>
    <div class="price-unit">per person*</div>
    <p class="price-note">*enquire for multi booking discounts for 2 people or more</p>
  </section>

  <div class="abs host-photo" role="img" aria-label="Photo of host Owen Calder seated in a red chair"></div>
  <section class="abs host">
    <div class="block-title">HOSTED &amp; FACILITED</div>
    <div class="block-rule"></div>
    <p class="host-name">Owen Calder</p>
    <p class="host-company">Portwell Business Coaching</p>
  </section>

  <div class="abs cta">REGISTER NOW</div>

  <footer class="abs footer">
    <div class="footer-brand">portwell<br>business coaching</div>
    <div class="footer-contact"><span>0400 555 182</span>|<span>owen@portwellcoaching.com.au</span>|<span>Network</span></div>
  </footer>

  <div class="abs social one" role="img" aria-label="Social link"></div>
  <div class="abs social two" role="img" aria-label="Social link"></div>
  <div class="abs social three" role="img" aria-label="Social link"></div>
  <div class="abs social four" role="img" aria-label="Social link"></div>
</div>
</body>
</html>
```